Polling website project

We need a website design for a polling website called vextiq.com. This will be a website where visitors can take and create polls for various topics along with view results. We want something really simple and "web 2.0." We are going to make a cell phone app that goes along with the website and we want the look and feel of the website to be very "app-like." Basically that means minimalistic design with a poll being the center of the page.
When someone comes to the site, we want them to see basically just a poll in the center of the screen and a toolbar at the top of the page with links to login fields/user profile, post a new poll, view friends list, a drop-down list of poll topics, and a search bar. We need about three pages mocked up: a home page/poll view page, a user control panel/profile page, a submit new poll page.
We also want our logo/header to have a "pulse" theme. The name vextiq is supposed to be a play on the word pulse, we'd like the logo to make that obvious, maybe the use of the EKG graph could work.
We also want a nice tab in the corner to sign up that is attractive and flashy, kind of like the feedback tab on the side of this website.
Target Market(s)
Teens and young adults, the chatterloop crowd
Industry/Entity Type
Cell Phone
Look and feel
Each slider illustrates characteristics of the customer's brand and the style your logo design should communicate.

```html
<!DOCTYPE html>
<html lang="en">
<head>
<meta charset="utf-8">
<title>Vextiq – Polls</title>
<link rel="stylesheet" href="https://fonts.googleapis.com/css2?family=Arimo:wght@400;700&family=Roboto+Condensed:wght@400;700&display=swap">
<style>
:root{
  --teal:#0a8585;
  --teal-dark:#067474;
  --teal-light:#1aa3a3;
  --white:#ffffff;
  --band:#f1f1f1;
  --text:#333333;
  --muted:#555555;
  --rule:#d6d6d6;
  --orange-top:#f3a31a;
  --orange-bot:#d26a0a;
  --blue-top:#2ca0f5;
  --blue-bot:#0b7fe6;
  --bar-top:#a9cc5c;
  --bar-bot:#6f9a2b;
}
*{box-sizing:border-box;margin:0;padding:0}
html,body{width:1200px;height:760px;overflow:hidden;background:var(--white)}
body{position:relative;font-family:Arimo,Arial,sans-serif;color:var(--text)}

.site-header{position:absolute;left:0;top:0;width:1200px;height:91px;background:var(--teal);border-bottom:1px solid #3aa0a0}
.brand{position:absolute;left:170px;top:22px;font-size:40px;color:var(--white);letter-spacing:1px;font-weight:400}
.search{position:absolute;left:864px;top:18px;width:191px;height:24px;background:var(--teal-light);border:1px solid #35b9b9}
.search svg{position:absolute;right:7px;top:4px}
.main-nav{position:absolute;left:599px;top:60px;display:flex;font-family:"Roboto Condensed",Arial,sans-serif;font-size:18px;color:var(--white)}
.main-nav a{color:var(--white);text-decoration:none;position:relative;height:29px}
.main-nav .sep{margin:0 18px}
.main-nav .current::after{content:"";position:absolute;left:-21px;right:-21px;bottom:0;height:3px;background:var(--white)}
.caret{font-size:11px;margin-left:8px;vertical-align:2px}

.hero{position:absolute;left:0;top:92px;width:1200px;height:352px;
  background:radial-gradient(ellipse at 62% 0%,#1a9a9a 0%,var(--teal) 45%,var(--teal-dark) 100%)}
.hero-title{position:absolute;left:167px;top:64px;font-size:35px;line-height:39px;font-weight:700;color:var(--white);width:400px}
.hero-copy{position:absolute;left:169px;top:160px;width:356px;font-size:14.6px;line-height:20px;color:var(--white)}

.cta-band{position:absolute;left:0;top:444px;width:1200px;height:95px;background:linear-gradient(#ffffff,var(--band));border-bottom:1px solid var(--rule)}
.btn{position:absolute;top:25px;height:47px;border-radius:3px;color:var(--white);font-size:20px;text-align:center;line-height:47px}
.btn-start{left:167px;width:152px;background:linear-gradient(var(--orange-top),var(--orange-bot));border:1px solid #c56a10}
.btn-signup{left:346px;width:161px;background:linear-gradient(var(--blue-top),var(--blue-bot));border:1px solid #1679d0}

.demo-window{position:absolute;left:598px;top:198px;width:418px;height:300px;background:#eaeaea;border:1px solid #c9c9c9;border-radius:4px;box-shadow:0 1px 3px rgba(0,0,0,.25);overflow:hidden}
.demo-toolbar{position:absolute;left:0;top:0;width:100%;height:33px;background:linear-gradient(#f4f4f4,#d9d9d9)}
.demo-nav{position:absolute;left:7px;top:8px;width:56px;height:18px;border:1px solid #a9a9a9;border-radius:3px;background:linear-gradient(#eee,#c9c9c9)}
.demo-url{position:absolute;left:72px;top:8px;width:338px;height:17px;background:var(--white);border:1px solid #bdbdbd;border-radius:3px;font-size:8.5px;color:#666;padding:3px 6px}
.demo-bar{position:absolute;left:0;top:33px;width:100%;height:26px;background:var(--teal);color:var(--white);font-size:14px;padding:5px 28px}
.poll-card{position:absolute;left:27px;top:75px;width:367px;height:230px;background:var(--white);box-shadow:0 0 3px rgba(0,0,0,.15)}
.poll-title{height:35px;border-bottom:1px solid #e3e3e3;padding:9px 19px;font-size:15.5px;color:#666}
.poll-option{position:absolute;left:27px;width:313px;font-size:13px;color:#444}
.poll-option .votes{position:absolute;right:6px;top:0;color:#999}
.poll-track{position:absolute;left:0;top:17px;width:313px;height:11px;border:1px solid #c8c8c8;background:linear-gradient(#fafafa,#e4e4e4)}
.poll-fill{height:100%;background:linear-gradient(var(--bar-top),var(--bar-bot));border-right:1px solid #5b7f22}
.vote-now{position:absolute;left:29px;top:184px;font-size:16px;color:#666}
.vote-now svg{vertical-align:-2px;margin-left:6px}
.demo-base{position:absolute;left:0;bottom:0;width:100%;height:7px;background:#cfcfcf}

.signup-tab{position:absolute;left:1160px;top:219px;width:44px;height:161px;background:linear-gradient(90deg,#13a0a0,var(--teal-dark));border:3px solid var(--white);border-right:none;box-shadow:0 0 4px rgba(0,0,0,.3)}
.signup-tab span{position:absolute;left:50%;top:56px;transform:translate(-50%,-50%) rotate(-90deg);font-family:"Roboto Condensed",Arial,sans-serif;font-weight:700;font-size:22px;color:var(--white);white-space:nowrap}
.signup-tab svg{position:absolute;left:9px;top:124px}

.features{position:absolute;left:172px;top:557px;width:850px;display:flex;gap:30px}
.feature{width:392px}
.feature h2{font-weight:400;font-size:17px;color:#222;margin-bottom:8px}
.feature p{font-size:12.4px;line-height:20px;color:var(--muted);text-align:justify;max-height:100px;overflow:hidden}

.site-footer{position:absolute;left:0;top:719px;width:1200px;height:41px;border-top:1px solid var(--rule);text-align:center;font-size:12.5px;color:#444;padding-top:20px}
</style>
</head>
<body>
<header class="site-header">
  <div class="brand">VEXTIQ</div>
  <div class="search">
    <svg width="14" height="14" viewBox="0 0 14 14" aria-hidden="true"><circle cx="6" cy="6" r="4.5" fill="none" stroke="#d8f2f2" stroke-width="1.4"/><line x1="9.3" y1="9.3" x2="13" y2="13" stroke="#d8f2f2" stroke-width="1.6"/></svg>
  </div>
  <nav class="main-nav">
    <a href="#">My profile</a><span class="sep">|</span>
    <a href="#" class="current">Post a new poll</a><span class="sep">|</span>
    <a href="#">View friends</a><span class="sep">|</span>
    <a href="#">Poll topics<span class="caret">▼</span></a>
  </nav>
</header>

<section class="hero">
  <h1 class="hero-title">Lorem Ipsum is simply Dummy text.</h1>
  <p class="hero-copy">Lorem Ipsum is simply dummy text of the printing and typesetting industry. Lorem Ipsum has been the industry's standard dummy text ever since the 1500s, when an unknown printer took a galley of type and scrambled it to make a type specimen book. It has survived not only five.centuries, but also the leap into electronic typesetting, remaining essentially unchanged.</p>
</section>

<section class="cta-band">
  <a class="btn btn-start">Get started</a>
  <a class="btn btn-signup">Sign up now</a>
</section>

<div class="demo-window">
  <div class="demo-toolbar">
    <div class="demo-nav">
      <svg width="56" height="18" viewBox="0 0 56 18" aria-hidden="true"><path d="M17 5 L11 9 L17 13Z" fill="#666"/><line x1="28" y1="1" x2="28" y2="17" stroke="#aaa"/><path d="M39 5 L45 9 L39 13Z" fill="#666"/></svg>
    </div>
    <div class="demo-url">www.vextiq.com</div>
  </div>
  <div class="demo-bar">VEXTIQ</div>
  <div class="poll-card">
    <div class="poll-title">Vextiq&nbsp; polling demo</div>
    <div class="poll-option" style="top:50px">Awesome<span class="votes">150 votes</span><div class="poll-track"><div class="poll-fill" style="width:97%"></div></div></div>
    <div class="poll-option" style="top:92px">Good<span class="votes">95 votes</span><div class="poll-track"><div class="poll-fill" style="width:55%"></div></div></div>
    <div class="poll-option" style="top:132px">ok<span class="votes">50 votes</span><div class="poll-track"><div class="poll-fill" style="width:24%"></div></div></div>
    <div class="vote-now">Vote now<svg width="20" height="14" viewBox="0 0 20 14" aria-hidden="true"><path d="M0 0 L9 7 L0 14Z M10 0 L19 7 L10 14Z" fill="#bbb"/></svg></div>
  </div>
  <div class="demo-base"></div>
</div>

<a class="signup-tab">
  <span>SIGN UP</span>
  <svg width="22" height="24" viewBox="0 0 22 24" aria-hidden="true"><circle cx="11" cy="7" r="6" fill="#fff"/><path d="M1 24 Q1 13 11 13 Q21 13 21 24Z" fill="#fff"/></svg>
</a>

<section class="features">
  <article class="feature">
    <h2>Lorem Ipsum is simply dummy</h2>
    <p>Lorem Ipsum is simply dummy text of the printing and typesetting industry. Lorem Ipsum has been the industry's standard dummy text ever since the 1500s, when an unknown printer took a galley of type and scrambled it to make a type specimen book. It has survived not only five.centuries, but also the leap into electronic typesetting, remaining essentially unchanged.</p>
  </article>
  <article class="feature">
    <h2>Lorem Ipsum is simply dummy</h2>
    <p>Lorem Ipsum is simply dummy text of the printing and typesetting industry. Lorem Ipsum has been the industry's standard dummy text ever since the 1500s, when an unknown printer took a galley of type and scrambled it to make a type specimen book. It has survived not only five.centuries, but also the leap into electronic typesetting, remaining essentially unchanged.</p>
  </article>
</section>

<footer class="site-footer">Copyright © 2012 Vextiq. Use of this website constitutes acceptance of our User Agreement and Privacy Policy</footer>
</body>
</html>
```